Shine Crew

I need a flyer and business cards to hand out at office buildings and country clubs introducing my new auto detailing business, SHINE CREW. Call or text 913-555-0147 for an appointment. Complete auto detailing done at their place or mine, and we offer pick -up and drop-off, if needed. I believe the flyer needs a car on it. Black, blue, and pink are my preferred colors. While you go about your day's business, whether playing 18 holes of golf or putting in 8 hours at the office, we will have your ride shining like a new penny when you're ready to roll!

```html
<!DOCTYPE html>
<html lang="en">
<head>
<meta charset="UTF-8">
<title>Shine Crew — Auto Detailing</title>
<link href="https://fonts.googleapis.com/css2?family=Poppins:ital,wght@0,700;0,800;1,700&display=swap" rel="stylesheet">
<style>
  :root {
    --navy: #0e1b3d;
    --navy-band: #17346f;
    --ink: #05070d;
    --white: #ffffff;
    --magenta: #c51fe0;
    --divider: #4f86e6;
  }
  * { margin: 0; padding: 0; box-sizing: border-box; }
  html, body { width: 1200px; height: 686px; overflow: hidden; background: var(--navy); }
  .card {
    position: relative;
    width: 1200px;
    height: 686px;
    background: var(--navy);
    font-family: "Poppins", Arial, sans-serif;
    color: var(--white);
    overflow: hidden;
  }
  .brand {
    position: absolute;
    left: 40px;
    top: 40px;
    width: 420px;
    height: 160px;
    display: flex;
    align-items: center;
    justify-content: center;
  }
  .brand-name {
    font-weight: 800;
    font-size: 50px;
    letter-spacing: 0.5px;
    color: var(--white);
    white-space: nowrap;
  }
  .divider {
    position: absolute;
    left: 489px;
    top: 31px;
    width: 3px;
    height: 172px;
    background: var(--divider);
  }
  .headline {
    position: absolute;
    left: 520px;
    width: 630px;
    top: 30px;
    text-align: center;
    font-weight: 800;
    font-size: 37px;
    line-height: 1.18;
    letter-spacing: -0.3px;
  }
  .accent { color: var(--magenta); }
  .service-note {
    position: absolute;
    left: 535px;
    top: 149px;
    width: 582px;
    height: 38px;
    background: var(--navy-band);
    display: flex;
    align-items: center;
    justify-content: center;
    font-weight: 700;
    font-style: italic;
    font-size: 19.5px;
    letter-spacing: 0.2px;
    white-space: nowrap;
  }
  .gallery {
    position: absolute;
    left: 0;
    top: 222px;
    width: 1200px;
    height: 292px;
    background: var(--ink);
  }
  .photo { position: absolute; top: 10px; height: 271px; }
  .photo-wrap { left: 0; width: 377px; background: linear-gradient(135deg, #b5202c 0%, #6e1620 55%, #c9ccd4 100%); }
  .photo-polish { left: 386px; width: 419px; background: linear-gradient(135deg, #2a2b30 0%, #8d8f95 50%, #3b2226 100%); }
  .photo-coat { left: 814px; width: 386px; background: linear-gradient(135deg, #2b2f36 0%, #121417 60%, #5b616b 100%); }
  .cta {
    position: absolute;
    left: 0;
    width: 1200px;
    top: 528px;
    text-align: center;
    font-weight: 800;
    font-size: 51px;
    line-height: 1.1;
    letter-spacing: -0.3px;
  }
</style>
</head>
<body>
  <main class="card">
    <div class="brand"><span class="brand-name">SHINE CREW</span></div>
    <div class="divider"></div>

    <h1 class="headline">Complete <span class="accent">auto detailing</span><br>done at your place or mine</h1>
    <p class="service-note">WE OFFER PICK -UP AND DROP-OFF, IF NEEDED</p>

    <section class="gallery">
      <div class="photo photo-wrap" role="img" aria-label="Gloved hands applying red wrap film to a car body with a heat gun"></div>
      <div class="photo photo-polish" role="img" aria-label="Rotary polisher buffing a glossy car panel"></div>
      <div class="photo photo-coat" role="img" aria-label="Gloved hand applying ceramic coating with an applicator block on a dark car"></div>
    </section>

    <p class="cta">Call or text <span class="accent">913-555-0147</span><br>for an appointment</p>
  </main>
</body>
</html>
```